Birthday Party Invitation

I need to create a "save the date" for my birthday party.
Text:

Save the Date
Saturday, 6 December 2014
9 pm
Club la Vereda, Lindenhofweg 42, 8005 Zürich
BLACK IT OUT
SAVE IT!
RESERVE THE TIME
WRITE IT DOWN
HOLD THE DATE to LET YOUR HAIR DOWN and Party with Me.

Target Market(s)

Friends

Industry/Entity Type

Club

Requirements
Must have
• I want the flyer to look classy and sexy at the same time.
Nice to have
• Picture on the left or right, then text white on black background. Maybe a simple frame. Not too playful, rather simple, elegant and no graphics. Just picture and text.

```html
<!DOCTYPE html>
<html lang="en">
<head>
<meta charset="utf-8">
<title>Save the Date – Birthday Party</title>
<link rel="stylesheet" href="https://fonts.googleapis.com/css2?family=Felipa&family=Great+Vibes&family=Arimo:ital,wght@1,400;1,500&family=Noto+Serif:ital,wght@1,700&display=swap">
<style>
  :root {
    --bg-deep: #5c0a2c;
    --bg-mid: #8d1546;
    --bg-glow: #d2379a;
    --photo-red: #8a1538;
    --photo-dark: #1a0a0c;
    --frame: #f4f1f3;
    --plaque-top: #5a1f8c;
    --plaque-bottom: #8b3fc4;
    --plaque-edge: #f07a2c;
    --ink: #ffffff;
    --ink-soft: #fbeef6;
    --script: "Felipa", cursive;
    --flourish: "Great Vibes", cursive;
    --plain: "Arimo", Arial, sans-serif;
    --numeral: "Noto Serif", Georgia, serif;
  }
  html, body {
    margin: 0;
    padding: 0;
    overflow: hidden;
    background: #2a0515;
  }
  .invitation-card {
    position: relative;
    width: 1200px;
    height: 776px;
    overflow: hidden;
    background:
      radial-gradient(ellipse 520px 360px at 1000px 470px, rgba(226, 70, 176, 0.85), rgba(226, 70, 176, 0) 70%),
      radial-gradient(ellipse 420px 300px at 520px 300px, rgba(190, 40, 120, 0.5), rgba(190, 40, 120, 0) 70%),
      linear-gradient(160deg, var(--bg-deep) 0%, var(--bg-mid) 45%, #a51f67 75%, var(--bg-deep) 100%);
    color: var(--ink);
  }
  .card-art {
    position: absolute;
    inset: 0;
  }
  .heading {
    position: absolute;
    left: 150px;
    top: 26px;
    margin: 0;
    font-family: var(--flourish);
    font-weight: 400;
    font-size: 84px;
    line-height: 1;
    color: var(--ink-soft);
    text-shadow: 0 2px 4px rgba(60, 0, 30, 0.6);
  }
  .save-the-date {
    position: absolute;
    left: 525px;
    top: 112px;
    margin: 0;
    font-family: var(--script);
    font-size: 40px;
    font-weight: 400;
    transform: rotate(-13deg);
    transform-origin: left bottom;
    text-shadow: 0 2px 3px rgba(60, 0, 30, 0.6);
  }
  .event-details {
    position: absolute;
    left: 735px;
    top: 112px;
    width: 412px;
    text-align: center;
    font-family: var(--plain);
    font-style: italic;
    color: var(--ink);
  }
  .event-details p { margin: 0; }
  .event-day { font-size: 29px; margin-top: 10px !important; }
  .event-date { font-size: 30px; margin-top: 4px !important; }
  .event-time { font-size: 30px; margin-top: -4px !important; }
  .numeral {
    font-family: var(--numeral);
    font-weight: 700;
    font-size: 44px;
  }
  .venue {
    font-size: 28px;
    line-height: 31px;
    margin-top: 22px !important;
    font-weight: 500;
  }
  .reminders {
    list-style: none;
    margin: 0;
    padding: 0;
    font-family: var(--script);
    font-size: 29px;
    text-shadow: 0 2px 3px rgba(60, 0, 30, 0.55);
  }
  .reminders li { position: absolute; white-space: nowrap; }
  .r1 { left: 524px; top: 328px; }
  .r2 { left: 582px; top: 386px; }
  .r3 { left: 630px; top: 446px; }
  .r4 { left: 682px; top: 506px; }
  .r5 { left: 716px; top: 566px; }
  .party-call {
    position: absolute;
    margin: 0;
    font-family: var(--script);
    font-size: 41px;
    text-shadow: 0 2px 3px rgba(60, 0, 30, 0.55);
    white-space: nowrap;
  }
  .party-call--line1 { left: 552px; top: 636px; }
  .party-call--line2 { left: 866px; top: 690px; }
</style>
</head>
<body>
<main class="invitation-card">
  <svg class="card-art" width="1200" height="776" viewBox="0 0 1200 776" aria-hidden="false">
    <defs>
      <linearGradient id="photoTone" x1="0" y1="0" x2="1" y2="1">
        <stop offset="0" stop-color="var(--photo-dark)"/>
        <stop offset="0.55" stop-color="var(--photo-red)"/>
        <stop offset="1" stop-color="#2a0c12"/>
      </linearGradient>
      <linearGradient id="plaqueTone" x1="0" y1="0" x2="1" y2="1">
        <stop offset="0" stop-color="var(--plaque-top)"/>
        <stop offset="1" stop-color="var(--plaque-bottom)"/>
      </linearGradient>
      <linearGradient id="glowBand" x1="0" y1="0" x2="1" y2="0">
        <stop offset="0" stop-color="#f070c0" stop-opacity="0"/>
        <stop offset="0.5" stop-color="#f070c0" stop-opacity="0.45"/>
        <stop offset="1" stop-color="#f070c0" stop-opacity="0"/>
      </linearGradient>
    </defs>

    <polygon class="accent-band" points="0,200 120,120 560,650 440,776 330,776" fill="url(#glowBand)"/>

    <g class="portrait-frame">
      <polygon points="50,128 471,116 510,607 92,691" fill="var(--frame)"/>
      <polygon points="62,140 460,129 497,598 101,680" fill="url(#photoTone)"
               role="img" aria-label="Photo of the host in a red velvet Santa dress and fur-trimmed hat"/>
    </g>

    <path class="event-plaque"
          d="M778,112 H1102 Q1104,138 1130,140 Q1158,142 1158,168 V352 Q1158,378 1130,380 Q1104,382 1102,408 H778 Q776,382 750,380 Q722,378 722,352 V168 Q722,142 750,140 Q776,138 778,112 Z"
          fill="url(#plaqueTone)" stroke="var(--plaque-edge)" stroke-width="4"/>
  </svg>

  <h1 class="heading">Invitation</h1>
  <h2 class="save-the-date">Save the Date</h2>

  <section class="event-details">
    <p class="event-day">Saturday</p>
    <p class="event-date"><span class="numeral">6</span> December 2014</p>
    <p class="event-time"><span class="numeral">9</span> pm</p>
    <p class="venue">Club la Vereda,<br>Lindenhofweg 42,<br>8005 Zürich</p>
  </section>

  <ul class="reminders">
    <li class="r1">Black It Out</li>
    <li class="r2">Save It!</li>
    <li class="r3">Reserve The Time</li>
    <li class="r4">Write It Down</li>
    <li class="r5">Hold The Date to</li>
  </ul>

  <p class="party-call party-call--line1">Let Your Hair Down and</p>
  <p class="party-call party-call--line2">Party with Me.</p>
</main>
</body>
</html>
```